Lorvena Aesthetic Doctor

I require an elegant, luxurious looking business card for my aesthetic business. I am a doctor and that will set me aside from competitors. I am planning to provide home and spa based treatments to clients with high expectations. I have attached my logo.

```html
<!DOCTYPE html>
<html lang="en">
<head>
<meta charset="utf-8">
<title>Lorvena Aesthetic Doctor – Business Card</title>
<link rel="stylesheet" href="https://fonts.googleapis.com/css2?family=Didact+Gothic&display=swap">
<style>
  :root {
    --backdrop: #e3e3e3;
    --card-white: #ffffff;
    --aqua-light: #63d2ee;
    --aqua-deep: #2db4d9;
    --ink-grey: #6f6f6f;
    --ink-soft: #9a9a9a;
    --accent-blue: #29a9d6;
    --divider: #c9c9c9;
  }
  * { margin: 0; padding: 0; box-sizing: border-box; }
  html, body {
    width: 1200px;
    height: 1007px;
    overflow: hidden;
    background: var(--backdrop);
    font-family: "Didact Gothic", "Century Gothic", sans-serif;
  }
  .stage {
    position: relative;
    width: 1200px;
    height: 1007px;
  }
  .card {
    position: absolute;
    width: 525px;
    height: 300px;
    border-radius: 2px;
    box-shadow: 0 14px 30px rgba(0,0,0,0.14), 0 2px 6px rgba(0,0,0,0.08);
  }

  /* Front: brand side */
  .card-front {
    left: 620px;
    top: 250px;
    background: linear-gradient(135deg, var(--aqua-light) 0%, var(--aqua-deep) 100%);
    color: var(--card-white);
  }
  .brand {
    position: absolute;
    left: 120px;
    top: 96px;
    display: flex;
    align-items: center;
    gap: 16px;
  }
  .brand-dot {
    width: 58px;
    height: 58px;
    border-radius: 50%;
    background: var(--card-white);
    opacity: 0.9;
    flex: none;
  }
  .brand-name {
    font-size: 44px;
    letter-spacing: 3px;
    line-height: 1;
    text-transform: uppercase;
  }
  .brand-tagline {
    display: block;
    font-size: 15px;
    letter-spacing: 3.5px;
    margin-top: 6px;
  }
  .front-web {
    position: absolute;
    left: 120px;
    top: 190px;
    font-size: 13px;
    letter-spacing: 3px;
  }

  /* Back: contact side */
  .card-back {
    left: 70px;
    top: 470px;
    background: var(--card-white);
    color: var(--ink-grey);
  }
  .identity {
    position: absolute;
    right: 200px;
    top: 78px;
    text-align: right;
  }
  .doctor-name {
    font-size: 24px;
    color: var(--ink-grey);
  }
  .credentials {
    font-size: 13px;
    color: var(--accent-blue);
    letter-spacing: 0.5px;
  }
  .qualification {
    font-size: 12px;
    color: var(--ink-soft);
    margin-top: 4px;
  }
  .divider {
    position: absolute;
    left: 340px;
    top: 80px;
    width: 1px;
    height: 92px;
    background: var(--divider);
  }
  .contacts {
    position: absolute;
    left: 356px;
    top: 100px;
    list-style: none;
    font-size: 13px;
    line-height: 22px;
    color: var(--ink-grey);
  }
  .contacts li {
    display: flex;
    align-items: center;
    gap: 8px;
  }
  .contacts svg {
    width: 12px;
    height: 12px;
    fill: var(--accent-blue);
    flex: none;
  }
  .services {
    position: absolute;
    left: 60px;
    top: 186px;
    font-size: 14px;
    line-height: 24px;
    color: var(--ink-soft);
  }
  .services .sep {
    color: var(--accent-blue);
    padding: 0 4px;
  }
</style>
</head>
<body>
<main class="stage">

  <section class="card card-front" aria-label="Business card front">
    <div class="brand">
      <span class="brand-dot"></span>
      <div class="brand-name">Lorvena<span class="brand-tagline">Aesthetic Doctor</span></div>
    </div>
    <p class="front-web">www.lorvena.co.nz</p>
  </section>

  <section class="card card-back" aria-label="Business card back">
    <div class="identity">
      <p class="doctor-name">Dr Elsa Marwen <span class="credentials">MRCPCH MD</span></p>
      <p class="qualification">Australasian Diploma of Aesthetic Medicine</p>
    </div>

    <span class="divider"></span>

    <ul class="contacts">
      <li>
        <svg viewBox="0 0 24 24" aria-hidden="true"><path d="M6.6 10.8a15.1 15.1 0 0 0 6.6 6.6l2.2-2.2a1 1 0 0 1 1-.25 11.4 11.4 0 0 0 3.6.57 1 1 0 0 1 1 1V20a1 1 0 0 1-1 1A17 17 0 0 1 3 4a1 1 0 0 1 1-1h3.5a1 1 0 0 1 1 1c0 1.25.2 2.45.57 3.6a1 1 0 0 1-.25 1z"/></svg>
        0800 555 014
      </li>
      <li>
        <svg viewBox="0 0 24 24" aria-hidden="true"><path d="M2 5h20v14H2zm2 2v.5l8 5 8-5V7l-8 5z"/></svg>
        elsa@lorvena.co.nz
      </li>
      <li>
        <svg viewBox="0 0 24 24" aria-hidden="true"><circle cx="12" cy="12" r="10"/></svg>
        www.lorvena.co.nz
      </li>
    </ul>

    <p class="services">
      Dermal injectables<span class="sep">•</span>Plasma facials<span class="sep">•</span>Microneedling<span class="sep">•</span>Skin boosters<br>
      Excessive sweating<span class="sep">•</span>Home and Spa Based Treatments
    </p>
  </section>

</main>
</body>
</html>
```